Premium Lawn fertiliser packaging - Looking for long term designer

*Update at bottom
I need a carefully considered, bold and professional packaging design for my new premium lawn fertiliser product. This contest is for a detailed front of the stand-up pouch packaging and once I’ve chosen a winner, they’ll be asked to create the layout for the back that links to the front as well. I have a full range of additional products that will also need designs and so I'm looking for someone who can do a great job here and who we can work with long term.

The front should include our logo for Brindley Turf Supply Direct and be titled “Meadow Rise Max” "Professional Lawn Fertiliser". The spring fertiliser tag line is "Awaken your lawn: Lush Greening, Lasting Health".
Beneath it, it then needs to include some important usage information and the key benefits along with some suitable graphic.

Key information to include:

Apply March - June
Treats 35-50 m2
16-3-8
+2%MgO + 1% Fe + 2.9% CaO (this is the chemical makeup of the fertiliser and needs to be fairly prominent. If you look at other professional fertiliser packaging, you'll see how it needs to compare).

Key features:
Premium fertiliser, used by professionals
Advanced greening with micro-nutrient complex
Dual action Nitrogen: Instant green boost & continuous feed for 3 months
Child & pet safe

Our brand colours are purple and green. Purple = #592999, Green = 3cb64a / 81d742 / 4d9d44

I think these colours look great against a white background.

Please make sure you look at our website as well to get an idea of our brand: www.brindleyturfsupply.co.uk

To help, I've attached images of competitors fertiliser packaging that I like the look of. I'm not looking for you to copy but just see what type of thing appeals to me, the standard I'm expecting and what I need to compete against....

In addition, I have also attached some potential images you may wish to try using in your design, although please feel free to use your own if you have something better. For the moment, the images are 'preview' images, but once I decide on a design and we agree on the correct image, I will download and send over a fully licensed version.

*** Update*** When submitting your design, can you submit it in 2 formats: The first as a fully printed custom stand-up pouch and the second as a full-size label stuck onto a standup pouch (whatever colour you think is right for your design - choose white if you are not sure). To explain, I've just discovered we won't be able to get full custom bags printed in time for the first run and so we will have to opt for the design to be printed on labels and fixed onto bags. I therefore need to choose a design that works in both formats as both a label on a standup pouch as well as a fully printed pouch. Many thanks.

Target Market(s)

Domestic home-owners

Industry/Entity Type

Lawn care. NOT AGRICULTURE OR FARMING

Font styles to use
Sans Serif

Requirements
Must have
• Presented in 2 formats - see update at bottom of description
Nice to have
• I quite like designs against a white background, although I’m open to other ideas as well.
Should not have
• Please do not include any people or faces in the design. The text should be solid in colour, so no graduated colour fill in the text or outline text. Please avoid over-busy or cluttered designs.

```html
<!DOCTYPE html>
<html lang="en">
<head>
<meta charset="utf-8">
<title>Meadow Rise Max – Professional Lawn Fertiliser</title>
<link rel="stylesheet" href="https://fonts.googleapis.com/css2?family=Cabin:wght@500;600;700&family=Roboto+Condensed:wght@500;600&display=swap">
<style>
  :root{
    --backdrop:#dcdbdc;
    --sky-top:#9fdbe6;
    --sky-mid:#cdeef2;
    --sky-haze:#eef6f7;
    --grass-dark:#3f9a2c;
    --grass-light:#86cf4a;
    --brand-purple:#592999;
    --purple-soft:#a77ad6;
    --brand-green:#3cb64a;
    --green-dark:#4d9d44;
    --green-lime:#81d742;
    --title-edge:#3a2a1c;
    --white:#ffffff;
    --ink-grey:#4a4a4a;
  }
  *{box-sizing:border-box;margin:0;padding:0}
  html,body{width:1200px;height:1200px;overflow:hidden}
  body{background:var(--backdrop);font-family:"Cabin",sans-serif;position:relative}

  .pouch-front{
    position:absolute;left:310px;top:30px;width:580px;height:1140px;
    border-radius:14px;overflow:hidden;
    background:linear-gradient(180deg,var(--sky-top) 0%,var(--sky-mid) 25%,var(--sky-haze) 55%,var(--sky-mid) 80%);
  }
  .sky-scene{position:absolute;inset:0;
    background:
      radial-gradient(ellipse 180px 60px at 200px 120px,rgba(255,255,255,.7),transparent 70%),
      radial-gradient(ellipse 220px 70px at 420px 180px,rgba(255,255,255,.6),transparent 70%),
      radial-gradient(ellipse 300px 260px at 290px 700px,rgba(255,255,255,.75),transparent 70%);}
  .meadow-scene{position:absolute;left:0;right:0;bottom:0;height:175px;
    background:linear-gradient(180deg,var(--grass-light) 0%,var(--grass-dark) 100%);
    border-radius:60% 40% 0 0 / 30% 25% 0 0;}
  .seal-line{position:absolute;left:0;right:0;top:118px;height:2px;background:rgba(255,255,255,.7)}

  .brand-mark{position:absolute;top:170px;left:0;right:0;display:flex;align-items:center;justify-content:center;gap:10px}
  .brand-mark .dot{width:22px;height:22px;border-radius:50%;background:var(--green-dark)}
  .brand-mark .name{font-weight:600;font-size:24px;color:var(--green-dark);letter-spacing:.5px}

  .product-title{position:absolute;top:292px;left:0;right:0;text-align:center;
    font-weight:700;font-variant:small-caps;color:var(--green-dark);
    font-size:92px;line-height:88px;
    -webkit-text-stroke:3px var(--title-edge);paint-order:stroke fill}
  .product-sub{position:absolute;top:482px;left:0;right:0;text-align:center;
    font-weight:700;font-variant:small-caps;font-size:33px;color:var(--white);
    -webkit-text-stroke:5px var(--title-edge);paint-order:stroke fill;letter-spacing:-.5px}

  .ribbon{position:absolute;left:50%;transform:translateX(-50%);
    background:var(--brand-purple);color:var(--white);font-weight:600;font-variant:small-caps;
    text-align:center;border-radius:4px;box-shadow:0 6px 10px rgba(60,20,110,.25);white-space:nowrap}
  .ribbon-lead{top:538px;width:248px;height:42px;font-size:26px;line-height:42px}
  .ribbon-tagline{top:598px;width:370px;height:52px;font-size:27px;line-height:52px}
  .ribbon-tagline::after{content:"";position:absolute;left:30px;right:30px;top:52px;height:40px;
    background:linear-gradient(180deg,rgba(89,41,153,.55),transparent);
    clip-path:polygon(0 0,100% 0,80% 100%,20% 100%)}

  .info-panel{position:absolute;left:108px;top:692px;width:364px;height:470px;
    background:var(--brand-purple);border:3px solid var(--white);border-radius:16px;
    box-shadow:0 0 0 5px rgba(167,122,214,.5)}
  .info-list{list-style:none;text-align:center;color:var(--white);margin-top:20px}
  .info-list li{font-weight:600;font-variant:small-caps;font-size:24px;line-height:29px;white-space:nowrap}
  .info-list .rule{width:140px;height:2px;margin:8px auto 9px;background:var(--purple-soft)}
  .info-list .analysis{font-size:24px}

  .feature-card{position:absolute;left:28px;top:208px;width:302px;height:246px;
    background:var(--white);border-radius:18px;display:grid;grid-template-columns:1fr 1fr;
    grid-template-rows:1fr 1fr;padding:12px 8px 6px;row-gap:4px}
  .feature{display:flex;flex-direction:column;align-items:center;text-align:center;
    font-family:"Roboto Condensed",sans-serif;color:var(--ink-grey)}
  .feature svg{width:58px;height:58px;flex:none}
  .feature p{font-size:12px;line-height:14px;margin-top:6px;font-weight:500}
  .feature small{display:block;font-size:9px;line-height:11px}
  .feature .safe-label{font-size:16px;line-height:17px}
</style>
</head>
<body>
  <main class="pouch-front">
    <div class="sky-scene" role="img" aria-label="Soft blue sky with light clouds"></div>
    <div class="meadow-scene" role="img" aria-label="Rolling green lawn hills with trees"></div>
    <div class="seal-line"></div>

    <header class="brand-mark">
      <span class="dot"></span>
      <span class="name">Brindley Turf Supply Direct</span>
    </header>

    <h1 class="product-title">Meadow Rise<br>Max</h1>
    <p class="product-sub">Professional Lawn Fertiliser</p>

    <div class="ribbon ribbon-lead">Awaken your lawn:</div>
    <div class="ribbon ribbon-tagline">Lush Greening, Lasting Health</div>

    <section class="info-panel">
      <ul class="info-list">
        <li>Apply March - June</li>
        <li class="rule"></li>
        <li>Treats 35-50 m2</li>
        <li class="rule"></li>
        <li class="analysis">16-3-8 +2%MgO + 1% Fe</li>
        <li class="analysis">+ 2.9% CaO</li>
      </ul>

      <div class="feature-card">
        <div class="feature">
          <svg viewBox="0 0 70 70" aria-hidden="true">
            <circle cx="35" cy="35" r="32" fill="var(--brand-green)"/>
            <circle cx="35" cy="35" r="22" fill="var(--white)"/>
            <circle cx="35" cy="35" r="18" fill="var(--brand-green)"/>
            <path d="M26 35l6 6 12-13" fill="none" stroke="var(--white)" stroke-width="5" stroke-linecap="round" stroke-linejoin="round"/>
          </svg>
          <p>Premium fertiliser,<br>used by professionals</p>
        </div>
        <div class="feature">
          <svg viewBox="0 0 70 70" role="img" aria-label="Grass icon">
            <g fill="none" stroke-linecap="round" stroke-width="4">
              <path d="M35 64C34 44 33 26 35 6" stroke="var(--green-dark)"/>
              <path d="M31 64C26 46 18 32 6 20" stroke="var(--brand-green)"/>
              <path d="M39 64C44 46 52 32 64 20" stroke="var(--brand-green)"/>
              <path d="M27 64C20 54 12 48 2 44" stroke="var(--green-lime)"/>
              <path d="M43 64C50 54 58 48 68 44" stroke="var(--green-lime)"/>
              <path d="M33 64C30 48 24 30 20 12" stroke="var(--green-lime)"/>
              <path d="M37 64C40 48 46 30 50 12" stroke="var(--green-dark)"/>
            </g>
          </svg>
          <p>Advanced greening with<br>micro-nutrient complex</p>
        </div>
        <div class="feature">
          <svg viewBox="0 0 70 70" aria-hidden="true">
            <path d="M35 5a30 30 0 1 0 30 30" fill="none" stroke="var(--brand-purple)" stroke-width="5"/>
            <path d="M35 5a30 30 0 0 1 30 30" fill="none" stroke="var(--brand-purple)" stroke-width="4" stroke-dasharray="3 5"/>
            <path d="M27 22h16M27 48h16M29 22c0 8 12 10 12 13s-12 5-12 13M41 22c0 8-12 10-12 13s12 5 12 13" fill="none" stroke="var(--brand-purple)" stroke-width="3"/>
          </svg>
          <p>Dual action Nitrogen:<small>Instant green boost &amp;<br>continuous feed for 3 months</small></p>
        </div>
        <div class="feature">
          <svg viewBox="0 0 70 70" role="img" aria-label="Safety shield icon">
            <path d="M35 4L60 13v20c0 16-11 27-25 33C21 60 10 49 10 33V13z" fill="var(--brand-green)"/>
            <path d="M24 35l8 8 15-16" fill="none" stroke="var(--white)" stroke-width="5" stroke-linecap="round" stroke-linejoin="round"/>
          </svg>
          <p class="safe-label">Child &amp;<br>pet safe</p>
        </div>
      </div>
    </section>
  </main>
</body>
</html>
```